Business card for hedge fund
Vornelle Capital Management
Project: Business card for hedge fund
Business card for hedge fund - Financial Services
Creative Brief
Professional
Wanrudee Halvorsen
Chief Operating Officer
wanru.halvorsen@vornellecap.example
2 additional names: Martin Gaskell, Portfolio Manager p: +1-555-382-4719 e-mail: martin.gaskell@vornellecap.example Jia Luo, Portfolio Manager p: +852-5123-9046 e: jia.luo@vornellecap.example No address to be included

```html
<!DOCTYPE html>
<html lang="en">
<head>
<meta charset="utf-8">
<title>Vornelle Capital Management — Business Card</title>
<link href="https://fonts.googleapis.com/css2?family=Cinzel:wght@400;600&display=swap" rel="stylesheet">
<style>
  :root {
    --backdrop: #d6d6d6;
    --card-top: #ffffff;
    --card-bottom: #e4e4e4;
    --ink: #2b2b2b;
    --ink-soft: #555555;
    --rule: #3a3a3a;
  }
  * { box-sizing: border-box; margin: 0; padding: 0; }
  html, body {
    width: 1200px; height: 901px; overflow: hidden;
    background: var(--backdrop);
    font-family: "Cinzel", "Times New Roman", serif;
    color: var(--ink);
  }
  .card {
    position: absolute; left: 100px; top: 165px;
    width: 1000px; height: 571px;
    border-radius: 34px;
    background: linear-gradient(160deg, var(--card-top) 0%, #f4f4f4 50%, var(--card-bottom) 100%);
    box-shadow: 0 18px 40px rgba(0,0,0,0.18);
  }
  .brand {
    position: absolute; left: 0; right: 0; top: 130px;
    text-align: center; font-weight: 400; color: var(--ink);
  }
  .brand-name { display: block; font-size: 64px; letter-spacing: 4px; line-height: 1; }
  .brand-line { display: block; font-size: 21px; letter-spacing: 3px; margin-top: 10px; }
  .identity {
    position: absolute; left: 55px; right: 55px; top: 370px;
    display: flex; align-items: baseline; gap: 14px;
    border-bottom: 1.5px solid var(--rule); padding-bottom: 10px;
  }
  .person-name { font-size: 34px; font-weight: 600; }
  .divider { font-size: 28px; color: var(--ink-soft); }
  .person-role { font-size: 25px; letter-spacing: 1px; }
  .contact {
    position: absolute; left: 55px; right: 55px; top: 452px;
    display: flex; align-items: center; gap: 12px;
    font-size: 19px; letter-spacing: 0.5px;
  }
  .contact-rule { flex: 1; height: 1.5px; background: var(--rule); }
  .contact-item { display: flex; align-items: center; gap: 9px; white-space: nowrap; }
  .contact-item svg { width: 20px; height: 20px; fill: var(--ink); }
</style>
</head>
<body>
  <div class="card">
    <div class="brand">
      <span class="brand-name">VORNELLE</span>
      <span class="brand-line">CAPITAL MANAGEMENT</span>
    </div>

    <div class="identity">
      <span class="person-name">Wanrudee Halvorsen</span>
      <span class="divider">|</span>
      <span class="person-role">Chief Operating Officer</span>
    </div>

    <div class="contact">
      <span class="contact-rule"></span>
      <span class="contact-item">
        <svg viewBox="0 0 24 24" aria-hidden="true"><path d="M6.6 10.8a15.1 15.1 0 0 0 6.6 6.6l2.2-2.2c.3-.3.7-.4 1-.2 1.1.4 2.3.6 3.6.6.6 0 1 .4 1 1V20c0 .6-.4 1-1 1A17 17 0 0 1 3 4c0-.6.4-1 1-1h3.5c.6 0 1 .4 1 1 0 1.3.2 2.5.6 3.6.1.3 0 .7-.2 1z"/></svg>
        +1-555-207-6418
      </span>
      <span class="divider">|</span>
      <span class="contact-item">
        <svg viewBox="0 0 24 24" aria-hidden="true"><path d="M2 5h20v14H2zm2 2v.5l8 5 8-5V7zm0 2.8V17h16V9.8l-8 5z"/></svg>
        wanru.halvorsen@vornellecap.example
      </span>
    </div>
  </div>
</body>
</html>
```